Glostiva: Graphic elements & webpage layout

Hi there! We’re building a site called Glostiva.example—it will be a community site for beauty product reviews, product recommendations and beauty tutorials. We've already got a logo, thanks to another CraftHive project. This project on CraftHive involves the following web design work:

1) Propose the overall graphic design elements of our site (according to our guidelines, which are in the attached file)

-Color Palette
-Fonts
-Icon set(s)

2) Using the overall graphic design elements in step 1 and our storyboard (attached), develop a webpage layout for the "How-to" page of our site. The "How-to" pages will be an editorial format, where our beauty journalist will show a video (and photos) of step-by-step beauty tutorials.

Please take a look at the attached files for a detailed brief and the logo! Thanks and we're looking forward to working with you!

Target Market(s)

Glostiva is for a French, English, and American audience of women between the ages of 16 and 30, who buy and use beauty products regularly.

Industry/Entity Type

Graphic Design

Requirements
Must have
• 1) A global set of graphic standards for the website Glostiva.example:
• A color palette
• Fonts
• An icon set (or sets)
• A menu
• Other graphic elements like button styles

2) A webpage layout (non-coded) for the How-To page template
(See storyboard, attached separately)
This webpage layout is for the main editorial format on Glostiva—step by step beauty tutorials. The individual on-page elements are in the storyboard, but overall we’d like it to look clean, friendly, and to encourage community participation and sharing on social networks.
Nice to have
• • A look and feel that is fresh, clean and modern
• Proximity: Establishes a close proximity with the user. (We want them to get the same feeling they get when talking beauty tips with their close friends).
• Neutrality: A sincere and neutral look and feel that doesn’t suggest a preference for any particular or elite type of beauty (but it can still be fun!)
• The graphic design is relevant to the beauty sector as a whole. (We could be talking about lipstick, a hairbrush or a man’s cologne)
• The graphic design alludes to the beauty industry (discreetly, not overtly!)
Should not have
• We've already got a logo, so you shouldn't suggest a new one!

We really want to avoid designs that are too traditionally "beauty" or too girly and feminine. Please no pink, no flowers, etc! :)

```html
<!DOCTYPE html>
<html lang="fr">
<head>
<meta charset="utf-8">
<title>Glostiva – How To</title>
<link href="https://fonts.googleapis.com/css2?family=Arvo:wght@700&family=Lato:ital,wght@0,400;0,700;1,700;1,900&family=Marcellus&display=swap" rel="stylesheet">
<style>
:root{
  --teal:#0f8a80;
  --teal-light:#25b3a5;
  --teal-dark:#07685f;
  --ink:#231f20;
  --paper:#f6f5ef;
  --line:#d7d5cf;
  --field:#efefec;
  --muted:#8a8a86;
}
*{box-sizing:border-box;margin:0;padding:0}
html,body{width:749px;height:1200px;overflow:hidden}
body{position:relative;background:var(--paper);font-family:"Lato",sans-serif;color:var(--ink)}
.abs{position:absolute}

.topbar{left:0;top:0;width:749px;height:25px;background:linear-gradient(var(--teal-light),var(--teal-dark))}
.lang{left:503px;top:7px;font-size:8px;font-style:italic;font-weight:700;color:#fff}
.social-dot{width:18px;height:18px;border-radius:50%;background:#0b6f66;border:1px solid #7fd6cd}

.header{left:0;top:25px;width:749px;height:72px;background:#fff;border-bottom:1px solid #e2e1dc}
.brand{left:123px;top:36px;font-family:"Arvo",serif;font-weight:700;font-size:34px;color:var(--ink);letter-spacing:-0.5px}
.nav-pill{height:25px;border-radius:13px;display:flex;align-items:center;justify-content:center;font-style:italic;font-weight:900;font-size:12px;color:#fff;border:2px solid #d9d9d6}
.nav-dark{background:linear-gradient(#3a3637,#0e0c0d)}
.nav-teal{background:linear-gradient(var(--teal-light),var(--teal-dark))}
.search{left:497px;top:54px;width:129px;height:18px;border-radius:9px;border:1px solid #cfd8d7;background:#f4fbfa;font-size:7px;color:#555;padding:4px 7px}
.search svg{position:absolute;right:6px;top:3px}

.title{left:121px;top:119px;font-family:"Marcellus",serif;font-size:19px;color:var(--teal);letter-spacing:.5px}
.share{top:121px;width:20px;height:20px;border-radius:4px;background:#3b74b9}
.meta{left:121px;top:149px;font-size:9px;font-weight:700;display:flex;gap:22px;align-items:baseline}
.meta b{font-weight:400;font-size:12px}
.meta .stars{display:inline-flex;gap:2px;vertical-align:-2px}

.video{background:var(--ink);border:1px solid #aaa}
.video .play{position:absolute;left:50%;top:50%;width:28px;height:28px;margin:-20px 0 0 -14px;border-radius:5px;background:#4a4546;display:flex;align-items:center;justify-content:center}
.controls{position:absolute;left:0;right:0;bottom:0;height:9px;background:linear-gradient(#e8e8e8,#bdbdbd);font-size:5px;font-weight:700;display:flex;align-items:center;gap:3px;padding:0 3px}
.controls .track{flex:1;height:2px;background:#8f8f8f}

.panel{background:#fff;border:1px solid var(--line)}
.list-head{font-style:italic;font-weight:700;font-size:8.5px;padding:7px 7px 6px}
.list li{list-style:none;margin:0 7px;height:15.8px;border-bottom:1px dotted #bbb;font-size:6.5px;display:flex;align-items:center;gap:4px}
.list li:last-child{border-bottom:none}
.view-all{font-size:6.5px;font-style:italic;color:var(--teal);text-align:right;padding-right:7px}

.copy{left:121px;width:340px;font-size:6.6px;font-weight:700;line-height:1.35}

.step{left:121px;width:90px;height:22px;border-radius:11px;font-style:italic;font-weight:900;font-size:11.5px;color:#fff;display:flex;align-items:center;justify-content:center;border:2px solid #ddd;letter-spacing:.5px}
.step-teal{background:linear-gradient(var(--teal-light),var(--teal-dark))}
.step-dark{background:linear-gradient(#3a3637,#0e0c0d)}

.tab{width:59px;height:17px;border-radius:7px 7px 0 0;font-style:italic;font-weight:900;font-size:8.5px;color:#fff;display:flex;align-items:center;justify-content:center}
.tab-on{background:var(--ink)}
.tab-off{background:var(--teal)}

.shop{display:grid;grid-template-columns:1fr 1fr;column-gap:2px;row-gap:13px;padding:3px 2px 0}
.card{display:flex;gap:3px;height:48px}
.thumb{width:40px;height:42px;border:1px solid #bbb}
.card .info{font-size:6.4px;font-weight:700;line-height:1.3}
.buy{margin-top:2px;width:33px;height:10px;border-radius:5px;background:var(--ink);color:#fff;font-size:6px;display:flex;align-items:center;justify-content:center;border:1px solid #999}
.shop-more{position:absolute;right:7px;bottom:4px;font-size:6.5px;color:var(--teal)}

.slider{background:var(--ink)}
.slide{position:absolute;left:21px;top:10px;width:294px;height:168px;border-radius:6px;background:linear-gradient(90deg,#5a4438 0%,#c9b7ab 30%,#eef1f2 50%,#dfe8ec 100%)}
.arrow{position:absolute;top:76px;width:27px;height:27px;border-radius:5px;background:rgba(120,120,120,.85);display:flex;align-items:center;justify-content:center}

.label{font-size:8px;font-weight:700}
.field{background:var(--field);border:1px solid #d8d8d4}
.textarea{font-size:8px;font-weight:700;padding:5px}
.submit{left:391px;top:1119px;width:67px;height:21px;border-radius:11px;background:linear-gradient(var(--teal-light),var(--teal-dark));border:2px solid #ddd;color:#fff;font-style:italic;font-weight:900;font-size:9px;display:flex;align-items:center;justify-content:center}

.footer{left:0;top:1155px;width:749px;height:45px;background:var(--ink)}
.footer p{position:absolute;left:122px;top:8px;width:380px;font-size:5.8px;color:#fff;line-height:1.55}
.footer .mark{position:absolute;left:556px;top:8px;font-family:"Arvo",serif;font-weight:700;font-size:16px;color:#fff}
.footer .year{position:absolute;left:587px;top:30px;font-size:5.5px;color:#fff}
</style>
</head>
<body>

<div class="abs topbar"></div>
<div class="abs lang">Choix de la langue</div>
<div class="abs social-dot" style="left:581px;top:3px" aria-label="Réseau social"></div>
<div class="abs social-dot" style="left:607px;top:3px" aria-label="Réseau social"></div>

<header class="abs header"></header>
<div class="abs brand">glostiva</div>
<div class="abs nav-pill nav-dark" style="left:316px;top:48px;width:97px">How To</div>
<div class="abs nav-pill nav-teal" style="left:420px;top:48px;width:66px">TIPS</div>
<div class="abs search">Search...
  <svg width="14" height="11" viewBox="0 0 14 11"><circle cx="5" cy="5" r="4" fill="none" stroke="var(--teal)" stroke-width="1.3"/><line x1="8" y1="7.5" x2="13" y2="10" stroke="var(--ink)" stroke-width="1.6"/></svg>
</div>

<h1 class="abs title">[TITRE DU TUTORIAL]</h1>
<div class="abs share" style="left:550px" aria-label="Partager"></div>
<div class="abs share" style="left:577px;background:#5cb6e4" aria-label="Partager"></div>
<svg class="abs" style="left:602px;top:119px" width="22" height="22" viewBox="0 0 24 24" aria-label="Favori"><path d="M12 1l3.2 7 7.6.7-5.8 5 1.8 7.5L12 17.3 5.2 21.2 7 13.7 1.2 8.7 8.8 8z" fill="#f3a11c" stroke="#c57a00" stroke-width=".8"/></svg>

<div class="abs meta">
  <span>Difficulté:
    <span class="stars">
      <svg width="11" height="11" viewBox="0 0 24 24"><path d="M12 1l3.2 7 7.6.7-5.8 5 1.8 7.5L12 17.3 5.2 21.2 7 13.7 1.2 8.7 8.8 8z" fill="var(--ink)"/></svg>
      <svg width="11" height="11" viewBox="0 0 24 24"><path d="M12 1l3.2 7 7.6.7-5.8 5 1.8 7.5L12 17.3 5.2 21.2 7 13.7 1.2 8.7 8.8 8z" fill="var(--ink)"/></svg>
      <svg width="11" height="11" viewBox="0 0 24 24"><path d="M12 1l3.2 7 7.6.7-5.8 5 1.8 7.5L12 17.3 5.2 21.2 7 13.7 1.2 8.7 8.8 8z" fill="#b5b5b2"/></svg>
    </span>
  </span>
  <span>Durée: <b>20 minutes</b></span>
  <span>Occasion: <b>Soirée</b></span>
</div>

<!-- Main video -->
<div class="abs video" style="left:121px;top:167px;width:337px;height:189px">
  <div class="play"><svg width="12" height="12" viewBox="0 0 12 12"><path d="M2 1l9 5-9 5z" fill="#fff"/></svg></div>
  <div class="controls"><span>▶ 00:00</span><span class="track"></span><span>00:00 ✕ ◂</span></div>
</div>

<aside class="abs panel" style="left:465px;top:166px;width:162px;height:192px">
  <div class="list-head">Les produits nécessaires</div>
  <ul class="list">
    <li>☑ Produit 1</li><li>☑ Produit 2</li><li>☑ Produit 3</li><li>☑ Produit 4</li><li>☑ Produit 5</li>
    <li>☑ Produit 6</li><li>☑ Produit 7</li><li>☑ Produit 8</li><li>☑ Produit 9</li><li>☑ Produit 10</li>
  </ul>
  <div class="view-all">+ View All Produit</div>
</aside>

<p class="abs copy" style="top:364px">Lorem ipsum dolor sit amet, maiores ornare ac fermentum, imperdiet ut vivamus a, nam lectus at nunc. Quam euismod sem, semper ut potenti pellentesque quisque. In eget sapien sed, sit duis vestibulum ultricies, placerat morbi amet vel, nullam in in lorem vel.</p>

<!-- Step 1 -->
<div class="abs step step-teal" style="top:405px">ETAPE 1</div>
<div class="abs tab tab-on" style="left:127px;top:441px">Vidéo</div>
<div class="abs tab tab-off" style="left:189px;top:441px">Photos</div>
<div class="abs video" style="left:121px;top:458px;width:337px;height:188px">
  <div class="play"><svg width="12" height="12" viewBox="0 0 12 12"><path d="M2 1l9 5-9 5z" fill="#fff"/></svg></div>
  <div class="controls"><span>▶ 00:00</span><span class="track"></span><span>00:00 ✕ ◂</span></div>
</div>

<aside class="abs panel" style="left:465px;top:456px;width:162px;height:191px">
  <div class="shop">
    <div class="card"><div class="thumb" role="img" aria-label="Photo de rouges à lèvres" style="background:linear-gradient(#fff,#d23a3a)"></div><div class="info">Produit 1<br>Marque<br>Prix<div class="buy">Acheter</div></div></div>
    <div class="card"><div class="thumb" role="img" aria-label="Photo de pots de crème" style="background:linear-gradient(#fff,#d98fb0)"></div><div class="info">Produit 1<br>Marque<br>Prix<div class="buy">Acheter</div></div></div>
    <div class="card"><div class="thumb" role="img" aria-label="Photo de flacons blancs" style="background:linear-gradient(#fff,#cfd3d6)"></div><div class="info">Produit 1<br>Marque<br>Prix<div class="buy">Acheter</div></div></div>
    <div class="card"><div class="thumb" role="img" aria-label="Photo de produits de soin" style="background:linear-gradient(#fff,#9ccfc3)"></div><div class="info">Produit 1<br>Marque<br>Prix<div class="buy">Acheter</div></div></div>
    <div class="card"><div class="thumb" role="img" aria-label="Photo de rouges à lèvres" style="background:linear-gradient(#fff,#e7a3a3)"></div><div class="info">Produit 1<br>Marque<br>Prix<div class="buy">Acheter</div></div></div>
    <div class="card"><div class="thumb" role="img" aria-label="Photo de rouge à lèvres" style="background:linear-gradient(#fff,#c91f2b)"></div><div class="info">Produit 1<br>Marque<br>Prix<div class="buy">Acheter</div></div></div>
  </div>
  <div class="shop-more">+ View All</div>
</aside>

<p class="abs copy" style="top:655px">Lorem ipsum dolor sit amet, maiores ornare ac fermentum, imperdiet ut vivamus a, nam lectus at nunc. Quam euismod sem, semper ut potenti pellentesque quisque. In eget sapien sed, sit duis vestibulum ultricies, placerat morbi amet vel, nullam in in lorem vel.</p>

<!-- Step 2 -->
<div class="abs step step-dark" style="top:696px">ETAPE 2</div>
<div class="abs tab tab-off" style="left:127px;top:735px">Vidéo</div>
<div class="abs tab tab-on" style="left:189px;top:735px">Photos</div>
<div class="abs slider" style="left:121px;top:751px;width:337px;height:189px">
  <div class="slide" role="img" aria-label="Photo beauté : portrait en gros plan à côté d'un flacon de soin"></div>
  <div class="arrow" style="left:3px"><svg width="10" height="12" viewBox="0 0 10 12"><path d="M8 1L3 6l5 5" fill="none" stroke="#fff" stroke-width="2.5"/></svg></div>
  <div class="arrow" style="right:3px"><svg width="10" height="12" viewBox="0 0 10 12"><path d="M2 1l5 5-5 5" fill="none" stroke="#fff" stroke-width="2.5"/></svg></div>
</div>

<aside class="abs panel" style="left:465px;top:750px;width:162px;height:192px">
  <div class="shop">
    <div class="card"><div class="thumb" role="img" aria-label="Photo de rouges à lèvres" style="background:linear-gradient(#fff,#d23a3a)"></div><div class="info">Produit 1<br>Marque<br>Prix<div class="buy">Acheter</div></div></div>
    <div class="card"><div class="thumb" role="img" aria-label="Photo de pots de crème" style="background:linear-gradient(#fff,#d98fb0)"></div><div class="info">Produit 1<br>Marque<br>Prix<div class="buy">Acheter</div></div></div>
    <div class="card"><div class="thumb" role="img" aria-label="Photo de flacons blancs" style="background:linear-gradient(#fff,#cfd3d6)"></div><div class="info">Produit 1<br>Marque<br>Prix<div class="buy">Acheter</div></div></div>
    <div class="card"><div class="thumb" role="img" aria-label="Photo de produits de soin" style="background:linear-gradient(#fff,#9ccfc3)"></div><div class="info">Produit 1<br>Marque<br>Prix<div class="buy">Acheter</div></div></div>
    <div class="card"><div class="thumb" role="img" aria-label="Photo de rouges à lèvres" style="background:linear-gradient(#fff,#e7a3a3)"></div><div class="info">Produit 1<br>Marque<br>Prix<div class="buy">Acheter</div></div></div>
    <div class="card"><div class="thumb" role="img" aria-label="Photo de rouge à lèvres" style="background:linear-gradient(#fff,#c91f2b)"></div><div class="info">Produit 1<br>Marque<br>Prix<div class="buy">Acheter</div></div></div>
  </div>
  <div class="shop-more">+ View All</div>
</aside>

<p class="abs copy" style="top:948px">Lorem ipsum dolor sit amet, maiores ornare ac fermentum, imperdiet ut vivamus a, nam lectus at nunc. Quam euismod sem, semper ut potenti pellentesque quisque. In eget sapien sed, sit duis vestibulum ultricies, placerat morbi amet vel, nullam in in lorem vel.</p>

<!-- Comments -->
<div class="abs step step-dark" style="top:991px;width:148px">COMMENTAIRES (12)</div>
<div class="abs label" style="left:121px;top:1024px">Nom</div>
<div class="abs field" style="left:146px;top:1020px;width:312px;height:15px"></div>
<div class="abs label" style="left:121px;top:1045px">Mail (n'apparaitra pas)</div>
<div class="abs field" style="left:211px;top:1041px;width:247px;height:16px"></div>
<div class="abs field textarea" style="left:121px;top:1063px;width:337px;height:48px">Laissez votre commentaire ici !</div>
<div class="abs submit">Commenter</div>

<footer class="abs footer">
  <p>Lorem ipsum dolor sit amet, maiores ornare ac fermentum, imperdiet ut vivamus a, nam lectus at nunc. Quam euismod sem, semper ut potenti pellentesque quisque. In eget sapien sed, sit duis vestibulum ultricies, placerat morbi amet vel, nullam in in lorem vel.<br>Commentaire de [nom] posté le [date]</p>
  <div class="mark">glostiva</div>
  <div class="year">© 2011</div>
</footer>

</body>
</html>
```